Karate Riverlands membership cards - one for black belts, one for everyone else.

Karate Riverlands needs designs for its membership cards which will be based on the Judo rank of the members; black belt and non black belt.

Karate Riverlands is a not-for-profit organisation set up to support the sport of Judo. Judo is an inexpensive, safe, dynamic contact sport, which is suitable for boys and girls, men and women.

Karate Riverlands is the State Sporting Organisation governing the sport of Judo in NSW and is supported by the Continental Games Council and Riverlands Bureau of Play & Leisure
Our mission is to be the leading state judo organisation in terms of membership, participation and achievement in all areas of the sport and its administration.

Specifications

Size: 54mm x 85.5mm (Standard credit card size)
Print: Full Colour
Corners: Rounded Corners
Sides: Double sided
Updates

Guys We've decided we want a QR code on the card Please incorporate this into your design Use this URL as a sample http://matfeesdesk.com.au/check/userid=12345

Target Market(s)

Existing Members

The Membership card should be a physical reminder to members that they are a part of something. The design of the card physically attractive so that the existing member can have a sense of pride carrying it around in his wallet. For some members, carrying a membership card is a status symbol and a way for them to show their pride of belonging to a specific group.

New Members

One of the objectives of Karate Riverlands is to Promote and market Judo as the Sport, Fitness and Physical Activity of choice amongst NSW residents. We are looking to attract more judo players everyday, the membership card can be used as an added marketing tool.

Kids aged 5-18

This demographic should also be considered for designs as this TA will also be holding membership cards.

Industry/Entity Type

Sporting Good

Contact Information for Business Card

See attachments of existing cards and logo

Requirements
Must have
• have 2 versions - the one for the black belts (higher grades, think black VORA) and the one for the lower grades (white background)
• Must address target market - you need to think about this.
• The cards purpose must be viewable above the wallet fold. ie top bar of card you see when you look in your wallet.
Nice to have
• Objectives:
• Card to be used as a marketing tool
• The main objective of having membership cards is to use it as a marketing tool. The design should have
• Differentiate Members based on Level
• Cards can be used to easily identify each membership level which in this case are two; Black Belt and Non-Black Belt. A change in color or design can make each level stand out.
• Data Gathering
• When using a membership card with a barcode, we as an organisation can gather data each time the member uses it to gain entry to a club or enter a competition The barcode can be. The data we collect can help us determine whether or not a a certain marketing activity should be continued and it can also help you craft our marketing message to target potential member’s interests.

```html
<!DOCTYPE html>
<html lang="en">
<head>
<meta charset="utf-8">
<title>Karate Riverlands Membership Cards</title>
<link rel="stylesheet" href="https://fonts.googleapis.com/css2?family=Arimo:wght@400;700&display=swap">
<style>
  :root {
    --stage: #6a8fc6;
    --band-light: #6f9ddb;
    --band-dark: #3f6cb0;
    --band-text: #1c2b4a;
    --black-card-top: #1f2740;
    --black-card-bottom: #131827;
    --white-card-top: #f2f4f8;
    --white-card-bottom: #dde2ea;
    --name-light: #d7dbe3;
    --name-dark: #23365c;
    --accent: #4f82c6;
    --detail-light: #e6e9ef;
    --detail-dark: #4f7fc0;
    --mark-dark: #5a79a8;
    --mark-light: #6f93c4;
  }
  * { margin: 0; padding: 0; box-sizing: border-box; }
  html, body { width: 1200px; height: 1200px; overflow: hidden; }
  body {
    background: var(--stage);
    font-family: "Arimo", Arial, sans-serif;
    position: relative;
  }
  .member-card {
    position: absolute;
    left: 184px;
    width: 832px;
    height: 524px;
    border-radius: 40px;
    overflow: hidden;
    box-shadow: 0 14px 30px rgba(10, 16, 36, 0.45);
  }
  .member-card--black { top: 36px; background: linear-gradient(180deg, var(--black-card-top), var(--black-card-bottom)); }
  .member-card--standard { top: 632px; background: linear-gradient(135deg, var(--white-card-top), var(--white-card-bottom)); }
  .card-band {
    height: 60px;
    background: linear-gradient(180deg, var(--band-light), var(--band-dark));
    color: var(--band-text);
    font-weight: 700;
    font-size: 29px;
    letter-spacing: 0.5px;
    text-align: center;
    line-height: 62px;
  }
  .member-rank {
    position: absolute; left: 66px; top: 190px;
    font-size: 24px; font-weight: 700; color: var(--name-light);
  }
  .member-name {
    position: absolute; left: 62px;
    font-size: 62px; font-weight: 700; letter-spacing: -0.5px; line-height: 1;
  }
  .member-card--black .member-name { top: 218px; color: var(--name-light); text-shadow: 0 3px 4px rgba(0,0,0,0.6); }
  .member-card--standard .member-name { top: 214px; color: var(--name-dark); }
  .member-number {
    position: absolute; left: 66px;
    font-size: 22px; font-weight: 700; color: var(--accent);
  }
  .member-card--black .member-number { top: 284px; }
  .member-card--standard .member-number { top: 278px; }
  .member-details {
    position: absolute; left: 66px; list-style: none;
    font-size: 17px; font-weight: 700; line-height: 22px;
  }
  .member-card--black .member-details { top: 366px; color: var(--detail-light); }
  .member-card--standard .member-details { top: 364px; color: var(--detail-dark); }
  .brand-mark {
    position: absolute; left: 560px; top: 150px; width: 220px;
    display: flex; flex-direction: column; align-items: center; gap: 26px;
  }
  .brand-mark__circle { width: 170px; height: 170px; border-radius: 50%; }
  .brand-mark__name {
    font-size: 28px; font-weight: 700; text-align: center; line-height: 1.1;
  }
  .member-card--black .brand-mark__circle { background: var(--mark-dark); opacity: 0.55; }
  .member-card--black .brand-mark__name { color: var(--detail-light); }
  .member-card--standard .brand-mark__circle { background: var(--mark-light); opacity: 0.35; }
  .member-card--standard .brand-mark__name { color: var(--mark-light); }
</style>
</head>
<body>
  <section class="member-card member-card--black">
    <header class="card-band">KARATE RIVERLANDS</header>
    <p class="member-rank">BLACK BELT</p>
    <h1 class="member-name">SAM CARVER</h1>
    <p class="member-number">MEMBER: 35388</p>
    <ul class="member-details">
      <li>DOB: 15/01/1970</li>
      <li>GENDER: MALE</li>
      <li>CLUB: RIVERSIDE UNI DOJO</li>
    </ul>
    <div class="brand-mark">
      <span class="brand-mark__circle"></span>
      <span class="brand-mark__name">KARATE RIVERLANDS</span>
    </div>
  </section>

  <section class="member-card member-card--standard">
    <header class="card-band">KARATE RIVERLANDS</header>
    <h2 class="member-name">SAM CARVER</h2>
    <p class="member-number">MEMBER: 35388</p>
    <ul class="member-details">
      <li>DOB: 15/01/1970</li>
      <li>GENDER: MALE</li>
      <li>CLUB: RIVERSIDE UNI DOJO</li>
    </ul>
    <div class="brand-mark">
      <span class="brand-mark__circle"></span>
      <span class="brand-mark__name">KARATE RIVERLANDS</span>
    </div>
  </section>
</body>
</html>
```